Financial Services General Marketing Brochure

Need a brochure to help recipients understand what makes HLC unique and the services that we offer. Must match look/feel of website https://harborlanecustody.example Layouts should make it easy to read the content - content should not be crammed into a traditional size/layout. Please see attached creative brief for specifics.

Target Market(s)

Financial advisors and mature couples looking for trustee services.

Industry/Entity Type

Financial Service

Colors
34a7d8
ffc214

Requirements
Must have
• See Creative Brief

```html
<!DOCTYPE html>
<html lang="en">
<head>
<meta charset="utf-8">
<title>Harbor Lane Custody – Brochure</title>
<link rel="stylesheet" href="https://fonts.googleapis.com/css2?family=Baloo+2:wght@600;700&family=Comfortaa:wght@400;600;700&family=Marcellus&display=swap">
<style>
  :root{
    --page-bg:#cfd1d5;
    --cream:#f8f2e7;
    --navy:#3b6485;
    --band:rgba(84,122,158,.86);
    --steel:#5b7fa0;
    --ink:#2e2e2e;
    --amber:#f2ab3a;
    --amber-light:#f7c45a;
    --rule:#5f86a8;
    --ring:#c9b59c;
    --white:#ffffff;
  }
  *{box-sizing:border-box;margin:0;padding:0}
  html,body{width:1059px;height:1200px;overflow:hidden}
  body{background:var(--page-bg);position:relative;font-family:"Comfortaa",sans-serif;color:var(--ink)}
  .spread{position:absolute;left:39px;width:980px;height:490px;background:var(--cream);overflow:hidden;box-shadow:0 10px 18px rgba(0,0,0,.18)}
  .spread--outside{top:54px}
  .spread--inside{top:606px}

  /* Outside spread */
  .services{position:absolute;left:17px;top:14px;width:265px}
  .services__title{font-family:"Marcellus",serif;font-size:22px;color:var(--navy);font-weight:400;letter-spacing:.3px;line-height:1}
  .services__title-rule{width:96px;height:1px;background:var(--rule);margin:3px 0 4px}
  .services__block{margin-bottom:6px}
  .services__head{font-family:"Comfortaa",sans-serif;font-weight:700;font-size:10.5px;color:var(--navy);line-height:13px}
  .services__text{font-size:8.8px;line-height:11.6px;color:var(--ink)}
  .services__list{list-style:none;font-size:8.8px;line-height:11.6px}
  .services__list li{padding-left:9px;position:relative;white-space:nowrap}
  .services__list li::before{content:"";position:absolute;left:0;top:3px;width:5px;height:5px;border:1px solid var(--ink);border-radius:50%}
  .services__list li::after{content:"";position:absolute;left:2px;top:2px;width:5px;height:3px;border-left:1.3px solid var(--ink);border-bottom:1.3px solid var(--ink);transform:rotate(-45deg)}
  .services__rule{width:96px;height:1px;background:var(--rule);margin:5px 0 6px}
  .contact{position:absolute;left:17px;top:412px;display:flex;align-items:flex-end;gap:14px}
  .brand-mark{display:flex;flex-direction:column;align-items:center;gap:4px;width:76px}
  .brand-mark__dot{width:22px;height:22px;border-radius:50%;background:var(--amber)}
  .brand-mark__name{font-family:"Marcellus",serif;font-size:12.5px;line-height:13px;color:var(--navy);text-align:center}
  .contact__details{border-top:1px solid var(--rule);padding-top:5px;font-size:8.4px;line-height:10.6px;color:var(--ink);margin-bottom:4px}
  .contact__details .contact__web{color:var(--steel)}

  .hero{position:absolute;left:288px;top:0;width:692px;height:490px}
  .hero__photo{position:absolute;inset:0;background:linear-gradient(180deg,#e9e4d6 0%,#cdbb98 35%,#9f7f56 70%,#a06b3c 100%)}
  .hero__band{position:absolute;left:0;top:292px;width:692px;height:181px;background:var(--band)}
  .hero__headline{position:absolute;left:250px;top:313px;width:400px;text-align:center;font-family:"Marcellus",serif;color:var(--white);font-size:19.5px;line-height:23.5px;letter-spacing:.4px;font-weight:400}
  .hero__brand{position:absolute;left:350px;top:400px;display:flex;align-items:center;gap:10px}
  .hero__brand .brand-mark__dot{width:30px;height:30px}
  .hero__brand-name{font-family:"Marcellus",serif;font-size:18px;line-height:19px;color:var(--white)}

  /* Inside spread */
  .story{position:absolute;left:17px;top:17px;width:472px;height:154px;background:var(--steel)}
  .story__text{position:absolute;left:11px;top:7px;width:281px;color:var(--white);font-size:9.4px;line-height:11.6px;text-align:justify}
  .story__text p+p{margin-top:11.6px}
  .story__portrait{position:absolute;left:318px;top:0;width:154px;height:154px;background:linear-gradient(160deg,#6d7d8c 0%,#3f5674 55%,#25334a 100%)}
  .story__caption{position:absolute;left:318px;bottom:0;width:154px;height:27px;background:rgba(84,122,158,.8);color:var(--white);font-size:9.2px;line-height:11.5px;padding:2px 0 0 31px}

  .unique{position:absolute;left:17px;top:180px;width:472px;height:292px;background:linear-gradient(90deg,var(--amber) 0%,var(--amber) 60%,var(--amber-light) 100%)}
  .unique__photo{position:absolute;right:0;top:0;width:190px;height:292px;background:linear-gradient(180deg,rgba(248,205,120,.5) 0%,rgba(222,170,80,.45) 100%)}
  .unique__title{position:absolute;left:12px;top:8px;font-family:"Baloo 2",sans-serif;font-weight:700;font-size:25px;line-height:30px;color:var(--navy)}
  .unique__list{position:absolute;left:12px;top:44px;width:281px;list-style:none}
  .unique__item{margin-bottom:9px}
  .unique__head{font-family:"Baloo 2",sans-serif;font-weight:700;font-size:12px;line-height:13px;color:var(--navy)}
  .unique__body{font-size:8.2px;line-height:10.2px;color:var(--ink);text-align:justify}
  .unique__rule{width:68px;height:1px;background:var(--navy);margin-top:6px}

  .team{position:absolute;left:500px;top:0;width:480px;height:490px}
  .team__title{position:absolute;left:0;top:26px;width:480px;text-align:center;font-family:"Comfortaa",sans-serif;font-weight:700;font-size:14.5px;line-height:17.5px;color:var(--navy)}
  .team__diagram{position:absolute;left:0;top:0;width:480px;height:490px}
  .team__diagram text{font-family:"Comfortaa",sans-serif}
</style>
</head>
<body>

<section class="spread spread--outside">
  <div class="services">
    <h1 class="services__title">OUR SERVICES</h1>
    <div class="services__title-rule"></div>

    <div class="services__block">
      <h2 class="services__head">What We Offer</h2>
      <p class="services__text">We specialize exclusively in the delivery of<br>trustee and estate fiduciary services.</p>
    </div>
    <div class="services__rule"></div>

    <div class="services__block">
      <h2 class="services__head">Who We Serve</h2>
      <p class="services__text">Families<br>Professional Advisors<br>Foundations</p>
    </div>
    <div class="services__rule"></div>

    <div class="services__block">
      <h2 class="services__head">How We Serve</h2>
      <p class="services__text">Our expertise and experience is in family wealth.<br>In this regard, we serve in the following ways:</p>
      <ul class="services__list">
        <li>Trustee (Trusts)</li>
        <li>Executor and Personal Representative (Will)</li>
        <li>Agent for Financial Affairs (Power of Attorney)</li>
        <li>Trust Protector</li>
        <li>Special Independent Trustee</li>
        <li>Consultant</li>
        <li>Expert Witness</li>
      </ul>
    </div>
    <div class="services__rule"></div>

    <div class="services__block">
      <h2 class="services__head">Trust Specialties</h2>
      <p class="services__text">The general types of trusts on which we serve as<br>trustee:</p>
      <ul class="services__list">
        <li>Family Trusts</li>
        <li>Charitable Trusts</li>
        <li>Family Foundations</li>
        <li>Life Insurance Trusts</li>
        <li>Retirement Trusts</li>
        <li>Special Needs Trusts</li>
      </ul>
    </div>
  </div>

  <div class="contact">
    <div class="brand-mark">
      <span class="brand-mark__dot"></span>
      <span class="brand-mark__name">Harbor Lane Custody</span>
    </div>
    <div class="contact__details">
      <span class="contact__web">harborlanecustody.example</span><br>
      555-014-2277<br>
      info@harborlanecustody.example
    </div>
  </div>

  <div class="hero">
    <div class="hero__photo" role="img" aria-label="Photo of a three-generation family running hand in hand through autumn leaves in a sunlit park"></div>
    <div class="hero__band"></div>
    <h2 class="hero__headline">HELPING FAMILIES PROTECT<br>AND ENRICH A<br>MULTI-GENERATIONAL HERITAGE</h2>
    <div class="hero__brand">
      <span class="brand-mark__dot"></span>
      <span class="hero__brand-name">Harbor Lane Custody</span>
    </div>
  </div>
</section>

<section class="spread spread--inside">
  <div class="story">
    <div class="story__text">
      <p>We understand that wealth and families is very complex. As families try to transfer wealth it can be an incredible blessing or, if done improperly, can be incredibly destructive. Often a neutral third party is needed to come alongside the family's advisory team to provide guidance as families go through their wealth transition.</p>
      <p>Our relational focus, and Open Circle approach, helps families to successfully navigate through the complexities of wealth, family and trusts. We believe a family "legacy" is about more than just money.</p>
    </div>
    <div class="story__portrait" role="img" aria-label="Portrait photo of the founding principal seated at a desk in a suit"></div>
    <div class="story__caption">Daniel Orwell, J.D.<br>Founding Principal</div>
  </div>

  <div class="unique">
    <div class="unique__photo" role="img" aria-label="Warm-toned photo of a mother walking hand in hand with her young daughter through a meadow"></div>
    <h2 class="unique__title">What Makes HLC Unique?</h2>
    <ol class="unique__list">
      <li class="unique__item">
        <h3 class="unique__head">1. Responsive</h3>
        <p class="unique__body">The family deals directly with decision makers instead of being subject to committees with whom the family may never have the opportunity to interact or engage.</p>
        <div class="unique__rule"></div>
      </li>
      <li class="unique__item">
        <h3 class="unique__head">2. Family Focus</h3>
        <p class="unique__body">We help families successfully navigate the complexities of family wealth, not just perform trust administration.</p>
        <div class="unique__rule"></div>
      </li>
      <li class="unique__item">
        <h3 class="unique__head">3. Independent</h3>
        <p class="unique__body">To avoid any conflicts of interest, we have no formal affiliations with wealth management firms or financial advisory practices.</p>
        <div class="unique__rule"></div>
      </li>
      <li class="unique__item">
        <h3 class="unique__head">4. Customized</h3>
        <p class="unique__body">Together we develop a customized approach that will best suit the family's needs.</p>
        <div class="unique__rule"></div>
      </li>
      <li class="unique__item">
        <h3 class="unique__head">5. Collaborative</h3>
        <p class="unique__body">We work collaboratively with the family's team of trusted professionals.</p>
      </li>
    </ol>
  </div>

  <div class="team">
    <h2 class="team__title">Harbor Lane Custody<br>Client/Family Centered Team</h2>
    <svg class="team__diagram" viewBox="0 0 480 490" width="480" height="490">
      <defs>
        <filter id="soft-shadow" x="-30%" y="-30%" width="160%" height="160%">
          <feDropShadow dx="2" dy="4" stdDeviation="3" flood-color="#000" flood-opacity=".18"/>
        </filter>
        <linearGradient id="tone-woman" x1="0" y1="0" x2="0" y2="1">
          <stop offset="0" stop-color="#8a6a55"/><stop offset="1" stop-color="#d9b8a0"/>
        </linearGradient>
        <linearGradient id="tone-babies" x1="0" y1="0" x2="0" y2="1">
          <stop offset="0" stop-color="#e7e4e3"/><stop offset="1" stop-color="#d8b9a6"/>
        </linearGradient>
        <linearGradient id="tone-couple" x1="0" y1="0" x2="1" y2="1">
          <stop offset="0" stop-color="#c9d6c0"/><stop offset="1" stop-color="#b88f78"/>
        </linearGradient>
      </defs>

      <g stroke="#d5ccbf" stroke-width="2" fill="none">
        <line x1="144" y1="222" x2="175" y2="222"/>
        <line x1="305" y1="222" x2="329" y2="222"/>
        <line x1="176" y1="116" x2="213" y2="166"/>
        <line x1="295" y1="119" x2="265" y2="166"/>
        <line x1="158" y1="332" x2="200" y2="290"/>
        <line x1="319" y1="332" x2="280" y2="290"/>
        <line x1="240" y1="394" x2="238" y2="290"/>
      </g>

      <g filter="url(#soft-shadow)">
        <circle cx="176" cy="116" r="49" fill="url(#tone-woman)" stroke="var(--ring)" stroke-width="3" role="img" aria-label="Photo of a smiling woman, the current beneficiary"/>
        <circle cx="295" cy="119" r="49" fill="url(#tone-babies)" stroke="var(--ring)" stroke-width="3" role="img" aria-label="Photo of two babies, the future beneficiaries"/>
        <circle cx="98" cy="222" r="46" fill="#fff" stroke="var(--ring)" stroke-width="3"/>
        <circle cx="375" cy="222" r="46" fill="#fff" stroke="var(--ring)" stroke-width="3"/>
        <circle cx="158" cy="332" r="46" fill="#fff" stroke="var(--ring)" stroke-width="3"/>
        <circle cx="319" cy="332" r="46" fill="#fff" stroke="var(--ring)" stroke-width="3"/>
        <circle cx="240" cy="394" r="46" fill="#fff" stroke="var(--ring)" stroke-width="3"/>
        <polygon points="197,162 279,162 320,226 279,290 197,290 156,226" fill="url(#tone-couple)" stroke="var(--ring)" stroke-width="3" role="img" aria-label="Photo of a smiling senior couple, the trust creators"/>
      </g>

      <g font-weight="700" fill="var(--navy)" text-anchor="middle">
        <text x="176" y="150" font-size="5.6" fill="#fff">Current Beneficiary</text>
        <text x="295" y="152" font-size="5.6" fill="#fff">Future Beneficiary</text>
        <text x="238" y="281" font-size="10.5" fill="#fff">Trust Creator</text>
        <text x="98" y="226" font-size="10.5">Attorney</text>
        <text x="375" y="226" font-size="10.5">Accountant</text>
        <text x="158" y="336" font-size="10.5">Financial</text>
        <text x="319" y="335" font-size="10.5">Trustee</text>
        <text x="240" y="383" font-size="9.2">Human Capital</text>
        <text x="240" y="395" font-size="9.2">Resources</text>
        <g font-family="Marcellus, serif" font-weight="400" font-size="4.6">
          <text x="240" y="405">Legacy Development</text>
          <text x="240" y="412">Health Care Management</text>
          <text x="240" y="419">Philanthropic Services</text>
          <text x="240" y="426">Life Coaching</text>
        </g>
      </g>
    </svg>
  </div>
</section>

</body>
</html>
```